HARLOWE CONSERVATORY SAXOPHONE SENIOR RECITAL

I need a poster design for my senior saxophone recital. The title of it is "Quill: a Voyage beneath the Edge of Tone". My concept is completely contrasting to the idea of a typical university recital. I'm so put off by the idea of "clap..clap..{play some music}..clap..clap..repeat". My recital is all based off of sound. The music I selected is all very modern (i.e Brem Ostrakel 'Warm from the First Pour' for Saxophone and Coffee Machine). I've included the Chatterbox link so you can see the picture I have in the background. I like the idea of minimal black and white photography. Also, I would like the time / date / location / etc. all included on it. Let your imaginations run wild! It's art for an artist!
https://www.chatterbox-example.net/events/412093857716230/
Target Market(s)
University Students around the Harlowe Conservatory and locals around the art district of South Beach, FL.
Industry/Entity Type
University
Look and feel

```html
<!DOCTYPE html>
<html lang="en">
<head>
<meta charset="utf-8">
<title>Quill: a Voyage beneath the Edge of Tone — Senior Recital</title>
<link rel="stylesheet" href="https://fonts.googleapis.com/css2?family=Questrial&family=Noto+Sans:wght@400;700&display=swap">
<style>
  :root {
    --sky: #8cc3df;
    --ink: #111111;
    --accent: #e8581c;
    --shade-deep: #1e2a31;
    --shade-mid: #4f6673;
  }
  * { margin: 0; padding: 0; box-sizing: border-box; }
  html, body { width: 850px; height: 1200px; overflow: hidden; }
  body { background: var(--sky); }
  .poster {
    position: relative;
    width: 850px;
    height: 1200px;
    background: var(--sky);
    overflow: hidden;
    color: var(--ink);
    font-family: "Noto Sans", Verdana, sans-serif;
  }
  .title {
    position: absolute;
    right: 65px;
    top: 66px;
    text-align: right;
    font-family: "Questrial", sans-serif;
    font-weight: 400;
    font-size: 66px;
    line-height: 57.5px;
    letter-spacing: 1px;
    text-transform: uppercase;
  }
  .title-lead { color: var(--accent); display: block; }
  .title-rest { display: block; }
  .skyline {
    position: absolute;
    left: 0;
    top: 445px;
    width: 850px;
    height: 305px;
  }
  .performer {
    position: absolute;
    left: 63px;
    top: 795px;
    font-size: 22px;
    line-height: 32px;
    letter-spacing: 0.5px;
  }
  .performer-name { font-weight: 700; }
  .venue {
    position: absolute;
    left: 63px;
    top: 1000px;
  }
  .venue-hall { font-size: 30px; line-height: 40px; letter-spacing: 0.3px; }
  .venue-school { font-size: 20px; line-height: 30px; letter-spacing: 0.5px; }
  .event-date {
    position: absolute;
    left: 68px;
    top: 1098px;
    font-size: 30px;
    font-weight: 700;
    letter-spacing: 0.8px;
    color: var(--accent);
  }
</style>
</head>
<body>
<main class="poster">
  <h1 class="title">
    <span class="title-lead">Quill:</span>
    <span class="title-rest">A Voyage<br>Beneath<br>The Edge<br>Of Tone</span>
  </h1>

  <svg class="skyline" viewBox="0 0 850 305" role="img" aria-label="Black and white photograph of a waterfront city skyline reflected in calm water">
    <defs>
      <linearGradient id="skyline-tone" x1="0" y1="0" x2="0" y2="1">
        <stop offset="0" stop-color="#8cc3df" stop-opacity="0"/>
        <stop offset="0.25" stop-color="#4f6673" stop-opacity="0.6"/>
        <stop offset="0.5" stop-color="#1e2a31"/>
        <stop offset="0.75" stop-color="#4f6673" stop-opacity="0.6"/>
        <stop offset="1" stop-color="#8cc3df" stop-opacity="0"/>
      </linearGradient>
    </defs>
    <rect x="0" y="0" width="850" height="305" fill="url(#skyline-tone)"/>
  </svg>

  <p class="performer">
    <span class="performer-name">DARIO VENTURELLI</span>, SAXOPHONE<br>
    Senior Recital
  </p>

  <div class="venue">
    <p class="venue-hall">Edwin T. Marsh Recital Hall</p>
    <p class="venue-school">HARLOWE CONSERVATORY</p>
  </div>

  <p class="event-date">Month 01, 2013 / 2:00 PM</p>
</main>
</body>
</html>
```